mobile app design: app provides timely Natural gas pipeline information (similar to weather, etc)

we are going to create and publish an app in all the three markets.( android, ios,windows). we have wire framed mostly all the screens. the designers are to provide the layout, design & background. The following are the most important things.

1. the app's target audience are guys working in the natural gas industry in the US.
2. the app provides the customer with latest pipeline information
3. the trial version is free and will provide information about one pipeline
4. slides 1 to 5 are trial version slides.
5. slides 6 onwards the customer chooses.
6. the final product is displayed in a grid.
7. the app will be developed using html5 and css3.
8. customer will pay per pipeline for the information. ( in app payment)
9 there are similiar ( complementary) products which provide weekly storage data at vexlo mart and quorbit app store.
10. i have attached the pdf document of the wireframe.
11.i have attached the logo
12. no name has been thought out yet.

Hi guys

I have a main question for the designer community .

1. is it possible to combine some of the pages ( screens  ) into one or two. use your gut feel. if not it is ok.

2. check out the flow, the color, the background , the font and the font size. it should be pleasing.

thanx

Tomek

Natural Gas

```html
<!DOCTYPE html>
<html lang="en">
<head>
<meta charset="utf-8">
<title>Pipelines – selection screen</title>
<link href="https://fonts.googleapis.com/css2?family=Open+Sans:wght@300;400;600&display=swap" rel="stylesheet">
<style>
  :root{
    --page:#f2f2f2;
    --teal:#5fb3a5;
    --teal-dark:#4c9d90;
    --status:#3b3b3b;
    --nav:#ececec;
    --body:#e2e2e2;
    --row:#f7f7f7;
    --box:#d6d6d6;
    --text:#6f6f6f;
    --muted:#8a8a8a;
    --tabbar:#363636;
    --button:#b9b9b9;
  }
  *{box-sizing:border-box;margin:0;padding:0}
  html,body{width:1185px;height:1200px;overflow:hidden;background:var(--page);font-family:"Open Sans",Arial,sans-serif}
  .screen{position:absolute;left:292px;top:67px;width:600px;height:1065px;background:var(--body);display:flex;flex-direction:column;overflow:hidden;box-shadow:0 2px 12px rgba(0,0,0,.12)}
  .status-bar{height:34px;background:var(--status);color:#eee;font-size:17px;font-weight:600;display:flex;align-items:center;justify-content:space-between;padding:0 14px}
  .status-bar .carrier{display:flex;align-items:center;gap:6px}
  .status-bar .battery{display:flex;align-items:center;gap:6px}
  .app-header{height:64px;background:var(--teal);color:#fff;font-size:27px;font-weight:400;display:flex;align-items:center;justify-content:center}
  .top-nav{height:62px;background:var(--nav);display:flex;align-items:center;justify-content:space-between;padding:0 28px;font-size:13px;color:var(--muted)}
  .top-nav .nav-item{display:flex;align-items:center;gap:10px}
  .pipeline-list{position:relative;list-style:none;padding:26px 70px 0 60px;flex:1}
  .pipeline-item{display:flex;align-items:center;height:43px}
  .check{width:22px;height:22px;flex:none;display:flex;align-items:center;justify-content:center;margin-right:18px}
  .check .box{width:15px;height:15px;background:var(--box)}
  .label{flex:1;height:22px;background:var(--row);font-size:14px;color:var(--text);padding:0 10px;line-height:22px;white-space:nowrap}
  .scroll-track{position:absolute;right:36px;top:22px;width:4px;height:440px;background:#cfcfcf;border-radius:2px}
  .scroll-thumb{position:absolute;right:36px;top:22px;width:4px;height:90px;background:#a8a8a8;border-radius:2px}
  .next-button{display:flex;justify-content:center;padding:6px 0 36px}
  .tab-bar{height:68px;background:var(--tabbar);display:flex;align-items:center;justify-content:space-between;padding:0 60px}
</style>
</head>
<body>
<main class="screen">
  <div class="status-bar">
    <span class="carrier">
      <svg width="22" height="12" viewBox="0 0 22 12"><rect x="0" y="8" width="3" height="4" fill="#eee"/><rect x="5" y="6" width="3" height="6" fill="#eee"/><rect x="10" y="4" width="3" height="8" fill="#eee"/><rect x="15" y="2" width="3" height="10" fill="#eee"/></svg>
      DINE
    </span>
    <span class="time">10:35 AM</span>
    <span class="battery">65%
      <svg width="30" height="14" viewBox="0 0 30 14"><rect x="1" y="1" width="25" height="12" rx="2" fill="none" stroke="#eee" stroke-width="1.5"/><rect x="3" y="3" width="14" height="8" fill="#eee"/><rect x="27" y="4" width="2" height="6" fill="#eee"/></svg>
    </span>
  </div>

  <header class="app-header">Pipelines</header>

  <nav class="top-nav">
    <span class="nav-item">
      <svg width="22" height="18" viewBox="0 0 22 18"><rect y="1" width="22" height="3" fill="var(--teal)"/><rect y="8" width="22" height="3" fill="var(--teal)"/><rect y="15" width="22" height="3" fill="var(--teal)"/></svg>
      Main Menu
    </span>
    <span class="nav-item">
      <svg width="24" height="24" viewBox="0 0 24 24"><circle cx="12" cy="12" r="12" fill="var(--teal)"/><text x="12" y="17" text-anchor="middle" font-size="14" font-weight="600" fill="#fff" font-family="Open Sans, sans-serif">$</text></svg>
      Payment
    </span>
    <span class="nav-item">
      <svg width="24" height="24" viewBox="0 0 24 24"><circle cx="12" cy="12" r="10.5" fill="none" stroke="var(--teal)" stroke-width="2"/><path d="M17 12H8M11.5 8 7.5 12l4 4" fill="none" stroke="var(--teal)" stroke-width="2"/></svg>
      To Trial version
    </span>
  </nav>

  <ul class="pipeline-list">
    <li class="pipeline-item"><span class="check"><svg width="22" height="18" viewBox="0 0 22 18"><path d="M2 9l6 6L20 2" fill="none" stroke="var(--teal)" stroke-width="3"/></svg></span><span class="label">Quillan Pipeline Company</span></li>
    <li class="pipeline-item"><span class="check"><span class="box"></span></span><span class="label">Ridgeway Express Pipeline</span></li>
    <li class="pipeline-item"><span class="check"><span class="box"></span></span><span class="label">Rubel Pipeline</span></li>
    <li class="pipeline-item"><span class="check"><span class="box"></span></span><span class="label">Southcrest Trails Pipeline</span></li>
    <li class="pipeline-item"><span class="check"><span class="box"></span></span><span class="label">Southfield Natural Gas Company</span></li>
    <li class="pipeline-item"><span class="check"><svg width="22" height="18" viewBox="0 0 22 18"><path d="M2 9l6 6L20 2" fill="none" stroke="var(--teal)" stroke-width="3"/></svg></span><span class="label">Southbay Star Central Gas Pipeline, Inc</span></li>
    <li class="pipeline-item"><span class="check"><span class="box"></span></span><span class="label">Sunvale</span></li>
    <li class="pipeline-item"><span class="check"><svg width="22" height="18" viewBox="0 0 22 18"><path d="M2 9l6 6L20 2" fill="none" stroke="var(--teal)" stroke-width="3"/></svg></span><span class="label">Tenbrook Gas Pipeline Company</span></li>
    <li class="pipeline-item"><span class="check"><span class="box"></span></span><span class="label">Terrace Eastern Transmission Pipeline</span></li>
    <li class="pipeline-item"><span class="check"><span class="box"></span></span><span class="label">Texmor Gas Pipe Line Corporation</span></li>
    <li class="pipeline-item"><span class="check"><svg width="22" height="18" viewBox="0 0 22 18"><path d="M2 9l6 6L20 2" fill="none" stroke="var(--teal)" stroke-width="3"/></svg></span><span class="label">Texmor Gas Transmission, LLC</span></li>
    <li class="pipeline-item"><span class="check"><span class="box"></span></span><span class="label">Tex-Orin Pipeline</span></li>
    <li class="pipeline-item"><span class="check"><span class="box"></span></span><span class="label">Trailwright Pipeline Company</span></li>
    <li class="pipeline-item"><span class="check"><span class="box"></span></span><span class="label">Transvale Pipeline</span></li>
    <span class="scroll-track"></span>
    <span class="scroll-thumb"></span>
  </ul>

  <div class="next-button">
    <svg width="96" height="96" viewBox="0 0 96 96" aria-label="Continue"><circle cx="48" cy="48" r="46" fill="var(--button)"/><circle cx="48" cy="48" r="26" fill="none" stroke="#fff" stroke-width="4"/><path d="M34 48h26M50 37l11 11-11 11" fill="none" stroke="#fff" stroke-width="4"/></svg>
  </div>

  <footer class="tab-bar">
    <svg width="22" height="18" viewBox="0 0 22 18"><rect y="1" width="22" height="3" fill="#ddd"/><rect y="8" width="22" height="3" fill="#ddd"/><rect y="15" width="22" height="3" fill="#ddd"/></svg>
    <svg width="26" height="26" viewBox="0 0 26 26"><circle cx="13" cy="13" r="13" fill="#ddd"/><text x="13" y="18" text-anchor="middle" font-size="15" font-weight="600" fill="var(--tabbar)" font-family="Open Sans, sans-serif">$</text></svg>
    <svg width="26" height="26" viewBox="0 0 26 26"><circle cx="13" cy="13" r="11.5" fill="none" stroke="#ddd" stroke-width="2"/><path d="M19 13H9M12.5 9 8.5 13l4 4" fill="none" stroke="#ddd" stroke-width="2"/></svg>
  </footer>
</main>
</body>
</html>
```